ZESTMUNCHY
Zestmunchy is a food van, serving high vibe delicious food to go. This business is dedicated to healthy delicious feel good food, beauty in service and a sustainable planet.

The van will operate in the south west of western Australia at music festivals events markets wherever people need great food to go!

I like the idea of vibrant green mixed with a yellow?? background with some rays like the sun through the background.
The font needs to say vibrant energetic
TO ME -vibrant energetic font has to appear to be on the move - perhaps with shading??

I like fusha if that works for font? but the colour has to say food too.

I would like a symbol on the card a simple V turned into a womans raised arms. This should be vibrant too.
Thank you
Blessings
Marisol

Target Market(s)

target lovers of healthy high vibe food. music festival goers. age 18- 50 feel. audiance conscious eaters of feel great food

Industry/Entity Type

Events

Contact Information for Business Card

ZESTMUNCHY
High Vibe Food
Van
Marisol -owner/opperator
0458170396
Face book symbol - ZESTMUNCHY

on the I would like a logo of a simple V turned into a womans arms up toward the sky flip side

My number and name again
Zestmunchy- feel great mobile food
Festivals, events, markets & where high vibe food 2 go is appreciated

Requirements
Nice to have
• Moving energetic font
colour that says high vibe and healthy food

a logo that is a simple V turned into a woman's raised arms in gratitude

```html
<!DOCTYPE html>
<html lang="en">
<head>
<meta charset="utf-8">
<title>Zestmunchy – Business Card</title>
<link href="https://fonts.googleapis.com/css2?family=Lilita+One&family=Fredoka:wght@600&display=swap" rel="stylesheet">
<style>
  :root {
    --page: #e9e6e1;
    --lime: #c6e23a;
    --lime-light: #e4f25a;
    --green: #5fb431;
    --fuchsia: #e5177f;
    --ink: #1a1a1a;
  }
  * { box-sizing: border-box; margin: 0; padding: 0; }
  html, body { width: 1200px; height: 723px; overflow: hidden; }
  body {
    background: var(--page);
    display: flex;
    align-items: center;
    justify-content: center;
    gap: 90px;
    font-family: "Fredoka", sans-serif;
  }
  .card {
    position: relative;
    width: 360px;
    height: 560px;
    overflow: hidden;
    box-shadow: 0 6px 18px rgba(0,0,0,.18);
  }
  .card__rays {
    position: absolute;
    inset: 0;
    background: radial-gradient(circle at 50% 40%, var(--lime-light) 0%, var(--lime) 40%, var(--green) 100%);
  }
  /* back */
  .back__figure {
    position: absolute;
    top: 0; left: 0;
    width: 360px; height: 300px;
    background: var(--fuchsia);
    border-bottom-left-radius: 180px 140px;
    border-bottom-right-radius: 180px 140px;
    border-bottom: 3px solid var(--ink);
  }
  .back__details {
    position: absolute;
    left: 28px; bottom: 40px;
    font-family: "Lilita One", sans-serif;
    font-size: 34px;
    line-height: 1.02;
    color: var(--fuchsia);
    -webkit-text-stroke: 1.5px var(--ink);
    text-transform: uppercase;
    letter-spacing: .5px;
  }
  /* front */
  .front__mark {
    position: absolute;
    top: 26px; left: 50%;
    transform: translateX(-50%);
    width: 104px; height: 104px;
    border-radius: 50%;
    background: var(--fuchsia);
  }
  .front__brand {
    position: absolute;
    top: 146px; left: 0; right: 0;
    text-align: center;
  }
  .brand-name {
    font-family: "Lilita One", sans-serif;
    font-size: 50px;
    color: var(--fuchsia);
    letter-spacing: 1px;
  }
  .tagline {
    font-size: 22px;
    color: var(--fuchsia);
    -webkit-text-stroke: .8px var(--ink);
    margin-top: -4px;
  }
  .front__contact {
    position: absolute;
    top: 270px; left: 0; right: 0;
    text-align: center;
    color: var(--fuchsia);
    -webkit-text-stroke: .8px var(--ink);
  }
  .contact-name { font-size: 30px; }
  .contact-role { font-size: 24px; margin-top: -4px; }
  .contact-phone { font-size: 30px; margin-top: 10px; letter-spacing: 1px; }
  .front__social {
    position: absolute;
    bottom: 46px; left: 0; right: 0;
    display: flex;
    flex-direction: column;
    align-items: center;
    gap: 8px;
  }
  .social-square {
    width: 34px; height: 34px;
    background: var(--fuchsia);
    border-radius: 6px;
  }
  .social-name {
    font-family: "Lilita One", sans-serif;
    font-size: 30px;
    color: var(--fuchsia);
    letter-spacing: 1px;
  }
</style>
</head>
<body>

  <section class="card card--back">
    <div class="card__rays" role="img" aria-label="Green and yellow sun rays bursting from the centre"></div>
    <div class="back__figure" role="img" aria-label="Green silhouette of a woman raising her arms to the sky on fuchsia"></div>
    <p class="back__details">Van Marisol<br>Owner/Operator<br>0458170396</p>
  </section>

  <section class="card card--front">
    <div class="card__rays" role="img" aria-label="Green and yellow sun rays bursting from the centre"></div>
    <div class="front__mark"></div>
    <div class="front__brand">
      <h1 class="brand-name">ZESTMUNCHY</h1>
      <p class="tagline">High Vibe Food Van</p>
    </div>
    <div class="front__contact">
      <p class="contact-name">Marisol</p>
      <p class="contact-role">owner/operator</p>
      <p class="contact-phone">0458170396</p>
    </div>
    <div class="front__social">
      <span class="social-square"></span>
      <span class="social-name">ZESTMUNCHY</span>
    </div>
  </section>

</body>
</html>
```